Flooring Company Wordpress Design Using Elementor

We need a website design using elementor for a flooring company. I have attached a word document with the entire content for the site. I have sample websites www.pellingtonrenovatesutah.com and www.stonepathtilesdenver.com

The site needs to look alot better than the samples. Modern and professional is what we are looking for. 100 times better than the sample websites.

I have images to be used in the site but the file is to large to attached here.

```html
<!DOCTYPE html>
<html lang="en">
<head>
<meta charset="utf-8">
<title>Keystone Flooring Florida</title>
<link href="https://fonts.googleapis.com/css2?family=Montserrat:ital,wght@0,300;0,400;0,500;0,600;0,700;1,400&display=swap" rel="stylesheet">
<style>
:root{
  --orange:#f7941d;
  --ink:#222;
  --body:#6d6d6d;
  --muted:#9a9a9a;
  --line:#e3e3e3;
  --light:#f7f7f7;
  --dark:#2a2a2a;
  --white:#fff;
}
*{box-sizing:border-box;margin:0;padding:0}
html,body{width:1200px;height:4152px;overflow:hidden;background:var(--white)}
body{font-family:'Montserrat',sans-serif;color:var(--ink);position:relative}
.abs{position:absolute}
.center{text-align:center}
.btn{position:absolute;display:flex;align-items:center;justify-content:center;border-radius:20px;font-size:11px;font-weight:600;letter-spacing:.5px;text-transform:uppercase;color:var(--white);background:var(--orange)}
.btn.ghost{background:transparent;border:2px solid var(--white);color:var(--orange)}
/* hero */
.hero{left:0;top:0;width:1200px;height:552px;background:linear-gradient(180deg,#2c2520 0%,#4a3628 45%,#6b4a30 80%,#3a2a20 100%)}
.brand{left:161px;top:42px;color:var(--white);font-size:15px;font-weight:600;line-height:22px;text-transform:uppercase}
.brand span{font-weight:400;font-size:13px}
.nav{left:690px;top:42px;display:flex;gap:38px;color:var(--white);font-size:11px;text-transform:uppercase}
.hero-title{left:0;top:206px;width:1200px;color:var(--orange);font-size:40px;font-weight:700}
.hero-sub{left:0;top:260px;width:1200px;color:var(--white);font-size:30px;font-weight:300}
.hero-text{left:320px;top:326px;width:560px;color:#e6e6e6;font-size:11.5px;line-height:20px}
/* features */
.feature{top:616px;width:332px;height:300px;border:1px solid var(--line);box-shadow:0 2px 6px rgba(0,0,0,.06);padding:0 26px}
.feature svg{display:block;margin:20px auto 0}
.feature h3{font-size:18px;font-weight:400;margin:18px 0 14px}
.feature p{font-size:10.5px;line-height:19.5px;color:var(--body)}
/* about */
.about-label{left:71px;top:1078px;color:var(--orange);font-size:11px;font-weight:500;text-transform:uppercase}
.about-h{left:71px;top:1097px;font-size:20px;font-weight:400}
.about-h2{left:70px;top:1125px;font-size:24px;font-weight:600}
.about-text{left:69px;top:1188px;width:470px;font-size:11px;line-height:22.5px;color:var(--body)}
.photo{position:absolute}
/* services */
.section-title{left:0;width:1200px;font-size:27px;font-weight:400}
.service{width:278px;height:472px;border:1px solid var(--line);box-shadow:0 2px 6px rgba(0,0,0,.06)}
.service .photo{left:0;top:0;width:276px;height:190px;position:relative}
.service h3{font-size:19px;font-weight:400;margin:20px 0 12px}
.service p{font-size:10.5px;line-height:18px;color:var(--body);padding:0 14px}
.service .btn{left:64px;bottom:22px;width:150px;height:30px;font-size:10.5px}
/* testimonial */
.band{left:0;top:2731px;width:1200px;height:311px;background:linear-gradient(90deg,#2e2a26,#4a4038 50%,#2f2b28)}
.band-title{left:0;top:2782px;width:1200px;color:var(--orange);font-size:27px;font-weight:400}
.quote{left:262px;top:2852px;width:676px;color:var(--white);font-size:12.5px;font-style:italic;line-height:22.5px}
.qmark{color:var(--orange);font-size:46px;font-weight:700;line-height:1}
.author{left:0;top:2942px;width:1200px;color:var(--orange);font-size:11px}
.dots{left:582px;top:2987px;display:flex;gap:8px}
.dots i{width:6px;height:6px;border-radius:50%;background:var(--white)}
.dots i:first-child{background:var(--orange)}
/* process */
.step{top:3180px;width:240px;margin-left:-120px}
.step .num{font-size:19px;color:#b8b8b8}
.step svg{display:block;margin:12px auto 0}
.step h4{font-size:15px;font-weight:400;margin:16px 0 12px}
.step p{font-size:10.5px;line-height:21px;color:var(--body);padding:0 10px}
/* form */
.form-bg{left:610px;top:3484px;width:590px;height:366px;background:var(--light)}
.form-title{left:645px;top:3522px;font-size:27px;font-weight:400}
.form-label{top:3580px;font-size:15px}
.field{position:absolute;width:234px;height:26px;border:1px solid #dcdcdc;background:var(--white);font-size:10.5px;padding:6px 12px;color:#444}
/* footer */
.footer{left:0;top:3931px;width:1200px;height:221px;background:linear-gradient(90deg,#1f1f1f,#2f2f2f 60%,#3b3a38)}
.foot-about{left:161px;top:3975px;width:280px;color:#e0e0e0;font-size:9.8px;line-height:19.5px}
.foot-col{top:3960px;color:var(--white)}
.foot-col h5{font-size:15px;font-weight:400;margin-bottom:14px}
.foot-col li{list-style:none;font-size:10.5px;line-height:20px;color:#dcdcdc}
.contact li{display:flex;align-items:center;gap:12px;line-height:30px}
.copy{left:0;top:4121px;width:1200px;color:#ccc;font-size:10.5px}
</style>
</head>
<body>

<!-- HERO -->
<div class="abs hero" role="img" aria-label="Dim interior of a home with wide wooden floorboards and tall windows"></div>
<div class="abs brand">Keystone Flooring<br><span>Florida</span></div>
<nav class="abs nav"><span>Home</span><span>About Us</span><span>Services</span><span>Contact Us</span></nav>
<h1 class="abs hero-title center">Experience Premium Flooring Installation</h1>
<p class="abs hero-sub center">In Central Florida with Keystone Group</p>
<p class="abs hero-text center">Are you tired of having your residential or commercial floors messed up by unprofessional services? Allow Keystone Group to change your floor installation and removal story today with our premium services, creativity, and personalized approach.</p>
<div class="btn ghost" style="left:398px;top:430px;width:134px;height:34px">Explore</div>
<div class="btn" style="left:571px;top:432px;width:199px;height:30px">Get Your Free Estimate</div>

<!-- FEATURES -->
<div class="abs feature center" style="left:55px">
  <svg width="40" height="40" viewBox="0 0 40 40" fill="none" stroke="#333" stroke-width="1.6"><circle cx="20" cy="22" r="12"/><path d="M20 15v7l5 3M14 6h12M20 6v4M32 10l3 3"/></svg>
  <h3>Minimal Stress On Your Plate</h3>
  <p>Floor installation or removal can be stressful for both parties. You have to relocate most of your property on the affected area to a new location and adjust your daily operation. The last thing we want to do is add to that. Hence, we take a proactive, customer-focused approach on all our floor installation. We will assist you with your property relocation and covering and ensure a quick and smooth process.</p>
</div>
<div class="abs feature center" style="left:426px">
  <svg width="40" height="40" viewBox="0 0 40 40" fill="none" stroke="#333" stroke-width="1.6"><path d="M8 14l6-7h12l6 7-12 17z"/><path d="M8 14h24M14 7l6 24M26 7l-6 24"/></svg>
  <h3>A Floor Worthy Of Your Home</h3>
  <p>The quality and type of your floor are as important as its style and appeal. The wrong combination could see you spending a lot on maintenance and feeling frustrated. That's why here at Keystone Group, don't just go with what is available, but what fits best. We will work with you to identify the kind of floor that matches your lifestyle, theme, preference, and strikes a balance between lower maintenance and durability.</p>
</div>
<div class="abs feature center" style="left:797px">
  <svg width="40" height="40" viewBox="0 0 40 40" fill="none" stroke="#333" stroke-width="1.6"><circle cx="20" cy="15" r="10"/><circle cx="20" cy="15" r="5"/><path d="M13 23l-4 12 5-2 3 4 3-8M27 23l4 12-5-2-3 4-3-8"/></svg>
  <h3>Qualified And Certified Experts</h3>
  <p>After spending a lot to finally get that property of your dream, the last thing you want is some rookie messing it up and getting you back on your plans. Here at Keystone Group, we understand this and strive to avoid its occurrence. Hence, we never assign your projects to unvetted professionals. Our team of experts is made up of only highly experienced and passionate individuals licensed in their specific fields to ensure the best results possible.</p>
</div>

<!-- ABOUT -->
<div class="abs about-label">Keystone Group comes with</div>
<div class="abs about-h">Over 14 Years Of experience In Floor Installation.</div>
<h2 class="abs about-h2">A Reliable Partner To Lean On</h2>
<p class="abs about-text">We are specialists when it comes to tile installation, hardwood installation, carpet installation, tile backsplash installation, vinyl installation, laminate floor installation, and floor removal. Over the years, we have come to position ourselves as the professional hands our customers need for all their installation and removal needs. With us, you can be assured of on-time performance, professional services, and prime craftsmanship.</p>
<div class="btn" style="left:65px;top:1325px;width:132px;height:31px">Learn More</div>
<div class="photo" style="left:600px;top:1027px;width:600px;height:360px;background:linear-gradient(135deg,#d9c2a0,#b58a5a 55%,#8a6a48)" role="img" aria-label="Bright bedroom with light wood floor, a white bed and a round side table"></div>

<!-- SERVICES -->
<h2 class="abs section-title center" style="top:1495px">Make Your Floors Scream Quality And Beauty</h2>

<div class="abs service center" style="left:161px;top:1600px">
  <div class="photo" style="background:linear-gradient(135deg,#2a2a2a,#5a5550 60%,#7a5a3a)" role="img" aria-label="Dark tiled floor beside a wooden chair"></div>
  <h3>Tile Installation</h3>
  <p>Tile is one durable flooring material that, when placed well, leaves your home or property looking luxurious and inviting. Keystone Group is fitted with expert tile installers who have experience installing anything tile, from tile flooring, bathroom tile, to backsplash tile. Allow us to make your home or business feel a little more like home.</p>
  <div class="btn">Get A Free Quote</div>
</div>
<div class="abs service center" style="left:461px;top:1600px">
  <div class="photo" style="background:linear-gradient(180deg,#d8cdb8,#8a5a32 60%,#5a3418)" role="img" aria-label="Polished hardwood floor in a sunlit room"></div>
  <h3>Hardwood Installation</h3>
  <p>Are you looking for the best hardwood installers near you? You are at the right place. Keystone Group is an expert in all kinds of hardwood installation, from solid to engineered hardwood. We will guide you toward choosing the right wood for your home or business to ensure your space is fixed with the best match.</p>
  <div class="btn">Get A Free Quote</div>
</div>
<div class="abs service center" style="left:761px;top:1600px">
  <div class="photo" style="background:linear-gradient(160deg,#3a3a3c,#7a7c80 55%,#9a9ca0)" role="img" aria-label="Grey laminate floor in a modern room"></div>
  <h3>Laminate Installation</h3>
  <p>Adorning your floor with laminate material is often a great option to limit scratches, wear and tear, and improve floor durability. With a lot to consider when it comes to picking the right flooring and having it installed, you need an experienced hand on your side. Allow our experts to come to your aid.</p>
  <div class="btn">Get A Free Quote</div>
</div>

<div class="abs service center" style="left:161px;top:2131px">
  <div class="photo" style="background:linear-gradient(180deg,#b89a78,#6a4a38 55%,#4a3028)" role="img" aria-label="Living room with brown wall-to-wall carpet"></div>
  <h3>Carpet Installation</h3>
  <p>Carpet installation is a good way to personalized the theme of your home, improve comfort, warmth, and a luxurious feel. With many carpets to choose from down to the tiring installation process, it can be overwhelming. Our team of professional carpet installers are here for you to help you neatly install the carpet that fits your home and floors</p>
  <div class="btn">Get A Free Quote</div>
</div>
<div class="abs service center" style="left:461px;top:2131px">
  <div class="photo" style="background:linear-gradient(180deg,#c9bca4,#a8a090 55%,#8c8a84)" role="img" aria-label="Kitchen with light cabinets and a vinyl floor"></div>
  <h3>Vinyl Installation</h3>
  <p>Vinyl flooring is a great option for families and businesses looking for a balance between the deep texture and feel of real wood, tiles, and stones with the durability, resistance, and low maintenance only dreamed of. Keystone Group is here to help you through your stages of vinyl floor installation. We will help you get the floor you want in no time at all</p>
  <div class="btn">Get A Free Quote</div>
</div>
<div class="abs service center" style="left:761px;top:2131px">
  <div class="photo" style="background:linear-gradient(135deg,#cfc8b8,#8a8478 50%,#4a4640)" role="img" aria-label="Old floorboards being pulled up during removal"></div>
  <h3>Floor Removal</h3>
  <p>Removing your floor isn't an easy task, whether it is a carpet installation, hardwood, or concrete. It takes a lot of time and is filled with risks. Keystone Group helps you save time and avoid sustaining any injury through the hands of our qualified floor demolition and removal professionals. We will handle both the removal and disposal for you.</p>
  <div class="btn">Get A Free Quote</div>
</div>

<!-- TESTIMONIAL -->
<div class="abs band" role="img" aria-label="Dimmed living room with wooden floor and an armchair"></div>
<h2 class="abs band-title center">Hear Their Stories!</h2>
<div class="abs qmark" style="left:228px;top:2862px">&ldquo;</div>
<p class="abs quote center">Lorem ipsum dolor sit amet, consectetur adipiscing elit, sed do eiusmod tempor incididunt ut labore et dolore magna aliqua. Quis ipsum suspendisse ultrices gravida. Risus commodo viverra maecenas accumsan lacus vel facilisis.</p>
<div class="abs qmark" style="left:948px;top:2858px">&rdquo;</div>
<div class="abs author center">-Dana Whitfield</div>
<div class="abs dots"><i></i><i></i><i></i></div>

<!-- PROCESS -->
<h2 class="abs section-title center" style="top:3105px">A Simple, Repeatable Process</h2>
<div class="abs step center" style="left:224px">
  <div class="num">01</div>
  <svg width="46" height="46" viewBox="0 0 46 46" fill="none" stroke="#333" stroke-width="1.6"><rect x="7" y="9" width="32" height="30" rx="2"/><path d="M7 17h32M14 5v8M32 5v8M13 23h4M21 23h4M29 23h4M13 30h4M21 30h4M29 30h4"/></svg>
  <h4>Schedule An Appointment</h4>
  <p>Fill out the form on our site or call us on our hotline to relay your needs and schedule a free site inspection. It is that simple!</p>
</div>
<div class="abs step center" style="left:486px">
  <div class="num">02</div>
  <svg width="46" height="46" viewBox="0 0 46 46" fill="none" stroke="#333" stroke-width="1.6"><rect x="7" y="7" width="32" height="32"/><path d="M7 20h14v19M21 28h18M29 7v13M13 12h10"/></svg>
  <h4>Your Preferred Floor material</h4>
  <p>Based on our findings on consultation and our inspection, we will help you figure out the right type of floor for your home or business space.</p>
</div>
<div class="abs step center" style="left:745px">
  <div class="num">03</div>
  <svg width="46" height="46" viewBox="0 0 46 46" fill="none" stroke="#333" stroke-width="1.6"><path d="M5 22L23 7l18 15M10 18v21h26V18"/><path d="M10 28h26M10 33h26M18 39V28M28 39V28"/></svg>
  <h4>Premium Installation</h4>
  <p>After the two stages are done, and you have approved the work date, our professionals for your floor will begin work on your property.</p>
</div>
<div class="abs step center" style="left:984px">
  <div class="num">04</div>
  <svg width="46" height="46" viewBox="0 0 46 46" fill="none" stroke="#333" stroke-width="1.6"><circle cx="22" cy="24" r="15"/><path d="M16 21h1M27 21h1M15 28c4 5 10 5 14 0M36 5v6M33 8h6"/></svg>
  <h4>A Happy You!</h4>
  <p>With a quality job done, go ahead and enjoy your floors for years to come with minimal maintenance on your side!</p>
</div>

<!-- GET STARTED -->
<div class="photo" style="left:0;top:3484px;width:610px;height:366px;background:linear-gradient(135deg,#2a2420,#5a4a3a 50%,#8a7058)" role="img" aria-label="Living room with a beige armchair on a wooden floor"></div>
<div class="abs form-bg"></div>
<h2 class="abs form-title">Get Started Now</h2>
<div class="abs form-label" style="left:649px">Your Info</div>
<div class="abs form-label" style="left:925px">Appointment</div>
<div class="field" style="left:648px;top:3617px">Name</div>
<div class="field" style="left:648px;top:3663px">Contact Info</div>
<div class="field" style="left:648px;top:3709px">Address</div>
<div class="field" style="left:924px;top:3617px">Type of appointment</div>
<div class="field" style="left:924px;top:3663px">Closest city</div>
<div class="field" style="left:924px;top:3709px">Date</div>
<div class="btn" style="left:827px;top:3770px;width:133px;height:30px">Submit</div>

<!-- FOOTER -->
<div class="abs footer" role="img" aria-label="Dark interior with wooden floor behind the footer"></div>
<p class="abs foot-about">Keystone Group comes with over 14 years of experience in floor installation. We are specialists when it comes to tile installation, hardwood installation, carpet installation, tile backsplash installation, vinyl installation, laminate floor installation, and floor removal</p>
<div class="abs foot-col" style="left:523px"><h5>Information</h5><ul><li>About Us</li><li>Customer</li><li>Service</li><li>Blog</li></ul></div>
<div class="abs foot-col" style="left:688px"><h5>Quick Links</h5><ul><li>Privacy Policy</li><li>Terms &amp; Conditions</li><li>Support</li><li>Contact Us</li></ul></div>
<div class="abs foot-col contact" style="left:855px"><h5>Contact Information</h5><ul>
  <li><svg width="12" height="14" viewBox="0 0 12 14"><path d="M6 0a5 5 0 0 0-5 5c0 4 5 9 5 9s5-5 5-9a5 5 0 0 0-5-5zm0 7a2 2 0 1 1 0-4 2 2 0 0 1 0 4z" fill="#fff"/></svg>Maple Grove Avenue, Orlando</li>
  <li><svg width="12" height="12" viewBox="0 0 12 12"><path d="M2.5 0.5l2 2.5-1.2 1.5a7 7 0 0 0 4.2 4.2L9 7.5l2.5 2-1.5 2C5 11 1 7 0.5 2z" fill="#fff"/></svg>(555) 010-2846</li>
  <li><svg width="13" height="10" viewBox="0 0 13 10"><rect x="0.5" y="0.5" width="12" height="9" fill="none" stroke="#fff"/><path d="M0.5 0.5l6 5 6-5" fill="none" stroke="#fff"/></svg>KeystoneGroup@mail.com</li>
</ul></div>
<div class="abs copy center">© 2020 © Keystone Group . All Rights Reserved.</div>

</body>
</html>
```